Business Card Design for Vantor Gear

We want to have a business card design for our company.
Company website: www.vantorgear-example.com.au
We looking for something cool, funky, and impressive, yet elegant.
Below are the contents that should be displayed on the card:
Front:
Name: Mark Dellow
Title: Sales & Purchasing
Company Name: Vantor Gear Pty Ltd
Phone: 02 5550 1473
Mobile: 0400 555 019
Email: mark@vantorgear-example.com.au
Website: www.vantorgear-example.com.au
Address: 17 Brackley St
Carrow Vale, NSW 2990
Back:
We buy sell new used Norvex and network equipment
• Huge Savings - save up to 95% off list prices
• Highest Reliability
• Comprehensive Warranty
• Fast delivery
• Large range of hardware in stock
Our logo can be downloaded at: www.vantorgear-example.com.au/logo.zip

```html
<!DOCTYPE html>
<html lang="en">
<head>
<meta charset="utf-8">
<title>Vantor Gear – Business Card</title>
<link href="https://fonts.googleapis.com/css2?family=Source+Sans+3:wght@400;600&display=swap" rel="stylesheet">
<style>
  :root {
    --page: #ffffff;
    --card-dark: #3c3c3c;
    --card-dark-light: #5b5b5b;
    --card-light: #ffffff;
    --yellow: #f2e200;
    --blue: #1b9ad8;
    --blue-deep: #0a58b8;
    --text-grey: #5a5a5a;
    --rule: #4a4a4a;
    --band-dark: #3a3a3a;
    --mark-orange: #f07a1e;
  }
  * { box-sizing: border-box; margin: 0; padding: 0; }
  html, body {
    width: 1200px; height: 900px; overflow: hidden;
    background: var(--page);
    font-family: "Source Sans 3", "Myriad Pro", sans-serif;
  }
  .canvas { position: relative; width: 1200px; height: 900px; }

  .card {
    position: absolute; left: 258px; width: 650px; height: 370px;
    overflow: hidden;
    box-shadow: 3px 5px 8px rgba(0,0,0,0.35);
  }

  /* ---------- back ---------- */
  .card--back {
    top: 42px;
    background: radial-gradient(ellipse at 55% 35%, var(--card-dark-light) 0%, var(--card-dark) 75%);
    color: #fff;
  }
  .card--back .decor-circle {
    position: absolute; left: 362px; top: 100px; width: 300px; height: 300px;
    border-radius: 50%;
    background: radial-gradient(circle at 40% 40%, rgba(240,122,30,0.28), rgba(27,154,216,0.18) 70%);
  }
  .brand { position: absolute; left: 50px; top: 36px; display: flex; align-items: center; }
  .brand__dot {
    width: 96px; height: 96px; border-radius: 50%;
    background: var(--mark-orange); margin-right: 30px; flex-shrink: 0;
  }
  .brand__text { display: flex; flex-direction: column; }
  .brand__name { font-weight: 600; font-size: 50px; line-height: 1; letter-spacing: -0.5px; }
  .brand__tagline {
    font-size: 11px; letter-spacing: 5.2px; margin-top: 8px; font-weight: 400;
  }
  .card--back .brand__name, .card--back .brand__tagline { color: #fff; }

  .offer { position: absolute; left: 48px; top: 164px; }
  .offer__heading {
    color: var(--yellow); font-weight: 600; font-size: 21px; line-height: 27px;
    margin-bottom: 7px;
  }
  .offer__list { list-style: none; }
  .offer__list li { font-size: 16px; line-height: 22px; color: #f2f2f2; }
  .offer__list li::before { content: "•"; color: var(--yellow); margin-right: 6px; }

  /* ---------- front ---------- */
  .card--front { top: 470px; background: var(--card-light); }
  .card--front .brand { left: 50px; top: 38px; }
  .card--front .brand__dot { width: 94px; height: 94px; margin-right: 26px; }
  .card--front .brand__name { color: var(--blue); font-size: 44px; }
  .card--front .brand__tagline { color: var(--text-grey); letter-spacing: 4.6px; }

  .person { position: absolute; right: 42px; top: 158px; text-align: right; }
  .person__name { color: var(--blue); font-weight: 600; font-size: 25px; line-height: 30px; }
  .person__role { color: var(--text-grey); font-size: 15px; line-height: 20px; }

  .rule { position: absolute; left: 42px; right: 0; top: 222px; height: 2px; background: var(--rule); }

  .company { position: absolute; left: 45px; top: 258px; font-size: 15px; line-height: 22px; color: var(--text-grey); }
  .company__name { color: var(--blue); font-size: 17px; }

  .contact { position: absolute; right: 42px; top: 236px; list-style: none; }
  .contact li {
    display: flex; align-items: center; justify-content: flex-end;
    font-size: 15px; line-height: 22px; color: var(--text-grey);
  }
  .contact svg { width: 17px; height: 17px; margin-left: 8px; }

  .band { position: absolute; left: 0; bottom: 0; width: 650px; height: 24px; }
</style>
</head>
<body>
<div class="canvas">

  <section class="card card--back" aria-label="Card back">
    <div class="decor-circle" role="img" aria-label="Large faint brand circle"></div>
    <div class="brand">
      <span class="brand__dot"></span>
      <div class="brand__text">
        <span class="brand__name">Vantor Gear</span>
        <span class="brand__tagline">NETWORKING EQUIPMENT</span>
      </div>
    </div>
    <div class="offer">
      <p class="offer__heading">We buy sell new used Norvex<br>and network equipment</p>
      <ul class="offer__list">
        <li>Huge Savings - save up to 95% off list prices</li>
        <li>Highest Reliability</li>
        <li>Comprehensive Warranty</li>
        <li>Fast delivery</li>
        <li>Large range of hardware in stock</li>
      </ul>
    </div>
  </section>

  <section class="card card--front" aria-label="Card front">
    <div class="brand">
      <span class="brand__dot"></span>
      <div class="brand__text">
        <span class="brand__name">Vantor Gear</span>
        <span class="brand__tagline">NETWORKING EQUIPMENT</span>
      </div>
    </div>

    <div class="person">
      <p class="person__name">Mark Dellow</p>
      <p class="person__role">Sales &amp; Purchasing</p>
    </div>

    <div class="rule"></div>

    <div class="company">
      <p class="company__name">Vantor Gear Pty Ltd</p>
      <p>17 Brackley St</p>
      <p>Carrow Vale, NSW 2990</p>
    </div>

    <ul class="contact">
      <li>02 5550 1473
        <svg viewBox="0 0 20 20"><circle cx="10" cy="10" r="10" fill="var(--blue)"/><path d="M6.5 5.5l2 0 1 2.5-1.2 1a6 6 0 0 0 2.7 2.7l1-1.2 2.5 1v2a1 1 0 0 1-1 1A8.5 8.5 0 0 1 5.5 6.5a1 1 0 0 1 1-1z" fill="#fff"/></svg>
      </li>
      <li>0400 555 019
        <svg viewBox="0 0 20 20"><circle cx="10" cy="10" r="10" fill="var(--blue)"/><rect x="7" y="4.5" width="6" height="11" rx="1" fill="none" stroke="#fff" stroke-width="1.4"/><circle cx="10" cy="13.3" r="0.8" fill="#fff"/></svg>
      </li>
      <li>mark@vantorgear-example.com.au
        <svg viewBox="0 0 20 20"><circle cx="10" cy="10" r="10" fill="var(--blue)"/><rect x="5" y="6.5" width="10" height="7" fill="#fff"/><path d="M5 6.5l5 4 5-4" fill="none" stroke="var(--blue)" stroke-width="1"/></svg>
      </li>
      <li>www.vantorgear-example.com.au
        <svg viewBox="0 0 20 20"><circle cx="10" cy="10" r="10" fill="var(--blue)"/><g fill="none" stroke="#fff" stroke-width="1.2"><circle cx="10" cy="10" r="5.5"/><ellipse cx="10" cy="10" rx="2.3" ry="5.5"/><path d="M4.5 10h11"/></g></svg>
      </li>
    </ul>

    <svg class="band" viewBox="0 0 650 24" preserveAspectRatio="none" aria-hidden="true">
      <defs>
        <linearGradient id="bandBlue" x1="0" x2="1">
          <stop offset="0" stop-color="var(--blue)"/>
          <stop offset="1" stop-color="var(--blue-deep)"/>
        </linearGradient>
      </defs>
      <polygon points="0,0 376,0 369,24 0,24" fill="var(--band-dark)"/>
      <polygon points="384,0 650,0 650,24 377,24" fill="url(#bandBlue)"/>
    </svg>
  </section>

</div>
</body>
</html>
```